Delivery Docket urgent plus require many other designs for more stationary after this.

We need a new delivery docket design urgently as the one we have needs updating and we have changed our company name. Please do not copy the one I have uploaded as we do not feel this looks professional enough. I uploaded it as a few designers requested to see what we are currently using thank you.
It is quite complex in that we need a range of information to be on the one docket.
We are a Transport Company based in Australia that has a wide variety of items that we deliver such as water, sand and gravels and heavy equipment transport.
We would prefer to keep this design to A5 size as we will get them made into books. We are looking for a modern professional look. Although it is only a delivery docket this is given to all our customers so needs to look impressive.

We need our new logo on the docket (PRW). There will also need to be areas for our address and contact numbers, email etc these will be supplied to the winning designer to make the final adjustments so for now just put something generic in these spaces.
Needs to have an area for customer details, purchase order number, date and docket number (docket number to be in red)
Needs a section where we can list the type of product / and or service that has been provided and the amount / qty usually 3 lines will be enough for this. Need area under this where the customer can sign name and print name to say that the goods / and or services have been received.

Also required somewhere on the docket are the words, Tax Invoice will be issued based on the information provided on this docket. Conditions on back of page

We then need a separate section on the same page which we will use internally that the staff member can tear off and hand into the office. On this section it needs to have area where the driver can list km at start of job and at end with space to calculate km travelled, details of fuel purchased eg amount and litres, vehicle that is being used. also need to log down wheel bearing temps.
prime mover needs spaces as follows
Steer axel FL____________ Steer axel FR _________ 1st drive axel L_______
1st drive axel R_________ 2nd drive axel L_______ 2nd drive axel R________

For the trailers need something similar x 2 as have 2 trailers
1st axel DS_________ 1st axel PS_________ 2nd axel DS__________
2nd axel PS_________ 3rd axel DS_________ 3rd axel PS__________

I have included a few examples of designs we have used in past and ones that we like so you can get an idea of the colours we prefer, I have included some of the designs we are currently receiving for our logo that I like so you can get idea again of colours we prefer. There is much more we need designed also such as time sheets, more delivery dockets and letter heads so there is a lot of more work available to the winning designer.

Thank you

Target Market(s)

Customers

Font styles to use
Serif
Sans Serif

Colors

Designer to choose colors to be used in the design.

Requirements
Should not have
• Please don't copy old docket as we do not like it and nned new info on new design thank you

```html
<!DOCTYPE html>
<html lang="en">
<head>
<meta charset="utf-8">
<title>PRW Delivery Docket</title>
<link href="https://fonts.googleapis.com/css2?family=Montserrat:ital,wght@0,300;0,400;0,600;0,700;0,800;1,400&display=swap" rel="stylesheet">
<style>
:root{
  --ink:#000;
  --red:#e0161b;
  --paper:#fff;
  --backdrop:#e9e9e9;
  --rule:#222;
  --faint:#dcdcdc;
}
*{box-sizing:border-box;margin:0;padding:0}
html,body{width:1072px;height:1200px;overflow:hidden}
body{background:var(--backdrop);font-family:"Montserrat",sans-serif;color:var(--ink);position:relative}
.docket{position:absolute;left:141px;top:39px;width:790px;height:1122px;background:var(--paper)}
.abs{position:absolute}
.hero-image{left:0;top:49px;width:340px;height:136px;background:linear-gradient(90deg,#d6d6d6 0%,#eaeaea 60%,rgba(255,255,255,0) 100%)}
.top-rule{left:46px;top:47px;width:700px;height:2px;background:var(--ink)}
.title-tag{left:297px;top:29px;width:198px;height:37px;background:var(--red);border:2px solid var(--ink);outline:2px solid var(--red);outline-offset:-5px;border-radius:5px;color:#fff;font-weight:800;font-size:18px;display:flex;align-items:center;justify-content:center}
.brand{left:315px;top:78px;width:160px;height:92px;display:flex;align-items:center;justify-content:center;font-weight:800;font-size:52px;letter-spacing:2px}
.panel{border:2px solid var(--ink);border-radius:8px;overflow:hidden}
.panel-head{background:var(--ink);color:#fff;height:34px;display:flex;align-items:center;font-weight:700}
.customer{left:48px;top:187px;width:697px;height:184px}
.customer .panel-head{justify-content:space-between;padding:0 16px}
.spaced{letter-spacing:5px;font-size:18px}
.docket-no{color:var(--red);font-size:18px;letter-spacing:0}
.fields{padding:12px 16px 0 16px}
.line{display:flex;align-items:flex-end;font-size:15px;height:34px;padding-bottom:6px;font-weight:400}
.fill{flex:1;border-bottom:2px dotted #555;margin:0 4px 4px 2px}
.dash{left:48px;width:697px;border-top:1.5px dashed var(--rule)}
.items{left:48px;top:394px;width:697px;height:242px}
.items table{width:100%;border-collapse:collapse;table-layout:fixed}
.items th{background:var(--ink);color:var(--red);height:31px;font-size:17px;font-weight:700}
.items th.qty{text-align:left;padding-left:16px;width:129px}
.items th.amt{text-align:right;padding-right:24px;width:165px}
.items td{height:35px;border-top:1.5px solid var(--ink);border-left:1.5px solid var(--ink)}
.items td:first-child,.items th:first-child{border-left:none}
.items th+th{border-left:2px solid #fff}
.tax-note{left:0;width:790px;top:642px;text-align:center;color:var(--red);font-style:italic;font-size:13.5px}
.vehicle{left:48px;top:673px;width:697px;height:134px}
.vehicle .panel-head{justify-content:center}
.vehicle .fields{padding:6px 10px 0 10px}
.vehicle .line{height:28px}
.axle-label{color:var(--red);font-size:13px;font-weight:400}
.axle-box{width:127px;height:21px;border:1.5px solid var(--ink)}
.sign{top:1012px;height:81px}
.sign .panel-head{height:27px;justify-content:center;font-weight:400;font-size:15px}
.received{left:40px;width:407px}
.signed{left:462px;width:283px}
</style>
</head>
<body>
<main class="docket">
  <div class="abs hero-image" role="img" aria-label="Faint photo of a tipper truck and trailers on an outback road"></div>
  <div class="abs top-rule"></div>
  <div class="abs title-tag">DELIVERY DOCKET</div>
  <div class="abs brand">PRW</div>

  <section class="abs panel customer">
    <div class="panel-head"><span class="spaced">CUSTOMER DETAILS</span><span class="docket-no">DELIVERY DOCKET NO.: 2050</span></div>
    <div class="fields">
      <div class="line">Business Name<span class="fill"></span>ABN<span class="fill" style="flex:0 0 180px"></span></div>
      <div class="line">Street/Address/Town<span class="fill"></span></div>
      <div class="line">Purchase Order No:<span class="fill"></span>Date<span class="fill" style="flex:0 0 160px"></span></div>
      <div class="line">Contact<span class="fill"></span></div>
    </div>
  </section>

  <div class="abs dash" style="top:382px"></div>

  <section class="abs panel items">
    <table>
      <thead><tr><th class="qty">Quantity</th><th>Description</th><th class="amt">Amount</th></tr></thead>
      <tbody>
        <tr><td></td><td></td><td></td></tr>
        <tr><td></td><td></td><td></td></tr>
        <tr><td></td><td></td><td></td></tr>
        <tr><td></td><td></td><td></td></tr>
        <tr><td></td><td></td><td></td></tr>
        <tr><td></td><td></td><td></td></tr>
      </tbody>
    </table>
  </section>

  <p class="abs tax-note">Tax invoice will be based on information provided on this docket. Condition on back of page.</p>
  <div class="abs dash" style="top:666px"></div>

  <section class="abs panel vehicle">
    <div class="panel-head"><span class="spaced">VEHICLE INFORMATION</span></div>
    <div class="fields">
      <div class="line">Km at start<span class="fill"></span>Km at end<span class="fill"></span>Km travelled<span class="fill"></span></div>
      <div class="line">Details of fuel purchased (litres)<span class="fill"></span>Amount<span class="fill"></span></div>
      <div class="line">Wheel bearing temps<span class="fill"></span></div>
    </div>
  </section>

  <div class="abs dash" style="top:818px"></div>

  <!-- Axle temperature grid -->
  <span class="abs axle-label" style="left:49px;top:830px">Steer axel FL</span><div class="abs axle-box" style="left:145px;top:828px"></div>
  <span class="abs axle-label" style="left:286px;top:830px">Steer axel FR</span><div class="abs axle-box" style="left:383px;top:828px"></div>
  <span class="abs axle-label" style="left:521px;top:830px">1st drive axel L</span><div class="abs axle-box" style="left:615px;top:828px"></div>

  <span class="abs axle-label" style="left:49px;top:858px">1st drive axel R</span><div class="abs axle-box" style="left:145px;top:856px"></div>
  <span class="abs axle-label" style="left:286px;top:858px">2nd drive axel L</span><div class="abs axle-box" style="left:383px;top:856px"></div>
  <span class="abs axle-label" style="left:521px;top:858px">2nd drive axel R</span><div class="abs axle-box" style="left:615px;top:856px"></div>

  <span class="abs axle-label" style="left:49px;top:888px">1st axel DS</span><div class="abs axle-box" style="left:145px;top:886px"></div>
  <span class="abs axle-label" style="left:286px;top:888px">1st axel PS</span><div class="abs axle-box" style="left:383px;top:886px"></div>
  <span class="abs axle-label" style="left:521px;top:888px">2nd axel DS</span><div class="abs axle-box" style="left:615px;top:886px"></div>

  <span class="abs axle-label" style="left:49px;top:916px">2nd axel PS</span><div class="abs axle-box" style="left:145px;top:914px"></div>
  <span class="abs axle-label" style="left:286px;top:916px">3rd axel DS</span><div class="abs axle-box" style="left:383px;top:914px"></div>
  <span class="abs axle-label" style="left:521px;top:916px">3rd axel PS</span><div class="abs axle-box" style="left:615px;top:914px"></div>

  <span class="abs axle-label" style="left:49px;top:943px">1st axel DS</span><div class="abs axle-box" style="left:145px;top:941px"></div>
  <span class="abs axle-label" style="left:286px;top:943px">1st axel PS</span><div class="abs axle-box" style="left:383px;top:941px"></div>
  <span class="abs axle-label" style="left:521px;top:943px">2nd axel DS</span><div class="abs axle-box" style="left:615px;top:941px"></div>

  <span class="abs axle-label" style="left:49px;top:971px">2nd axel PS</span><div class="abs axle-box" style="left:145px;top:969px"></div>
  <span class="abs axle-label" style="left:286px;top:971px">3rd axel DS</span><div class="abs axle-box" style="left:383px;top:969px"></div>
  <span class="abs axle-label" style="left:521px;top:971px">3rd axel PS</span><div class="abs axle-box" style="left:615px;top:969px"></div>

  <section class="abs panel sign received"><div class="panel-head">Good Received By</div></section>
  <section class="abs panel sign signed"><div class="panel-head">Signed</div></section>
</main>
</body>
</html>
```